Web Design Project - Velvet Hour service

Shall be a social community to set private dates for Velvet Hour service.
Main function is to
* Search / View / Contact / Recommend profiles
* Contact profiles

Industry/Entity Type

Escort

```html
<!DOCTYPE html>
<html lang="en">
<head>
<meta charset="utf-8">
<title>Velvet Hour — Get In Touch</title>
<link href="https://fonts.googleapis.com/css2?family=Cinzel+Decorative:wght@700&family=Cormorant+Garamond:ital,wght@1,600&family=Fraunces:opsz,wght@72,800&display=swap" rel="stylesheet">
<style>
  :root {
    --page: #2b2b2b;
    --bar-light: #d9b57a;
    --bar-dark: #a8814a;
    --bar-edge: #1e1e1e;
    --column: #3b0c0f;
    --column-top: #3d0000;
    --gold: #d4b06a;
    --tan: #7c4e1e;
    --frame: #9c6b2a;
    --field: #5a0f13;
    --ink: #1a0606;
    --silhouette-a: #120304;
    --silhouette-b: #3a0607;
  }
  * { box-sizing: border-box; margin: 0; padding: 0; }
  html, body { width: 1200px; height: 900px; overflow: hidden; }
  body { background: var(--page); position: relative; font-family: Arial, Helvetica, sans-serif; }

  .top-bar {
    position: absolute; left: 0; top: 0; width: 1200px; height: 62px;
    background: linear-gradient(var(--bar-edge) 0 10px, var(--bar-light) 10px, var(--bar-dark) 56px, var(--bar-edge) 58px);
  }
  .nav a {
    position: absolute; top: 24px; font-family: "Fraunces", Georgia, serif; font-weight: 800;
    font-size: 17px; color: var(--ink); text-decoration: none; white-space: nowrap;
  }

  .column {
    position: absolute; left: 257px; top: 62px; width: 766px; height: 838px;
    background: linear-gradient(#4a0d10 0, var(--column) 40%, #2e080a 100%);
  }
  .column-head { position: absolute; left: 0; top: 0; width: 100%; height: 81px; background: var(--column-top); }
  .brand {
    position: absolute; left: 0; top: 4px; width: 100%; text-align: center;
    font-family: "Cormorant Garamond", Georgia, serif; font-style: italic; font-weight: 600;
    font-size: 50px; color: var(--gold);
  }

  .ribbon { position: absolute; left: 436px; top: 148px; }
  .page-title {
    position: absolute; left: 436px; top: 150px; width: 394px; text-align: center;
    font-family: "Cormorant Garamond", Georgia, serif; font-style: italic; font-weight: 600;
    font-size: 40px; color: #4a0c0e;
  }
  .intro {
    position: absolute; left: 320px; top: 256px; width: 700px; text-align: center;
    font-family: "Cormorant Garamond", Georgia, serif; font-style: italic; font-weight: 600;
    font-size: 27px; line-height: 29px; color: var(--gold);
  }

  .figure {
    position: absolute; left: 172px; top: 165px; width: 168px; height: 475px;
    background: linear-gradient(90deg, var(--silhouette-a), var(--silhouette-b) 60%, var(--silhouette-a));
    border-radius: 40px 40px 6px 6px;
  }

  .field {
    position: absolute; left: 356px; width: 526px; height: 46px;
    border: 3px solid var(--frame); background: var(--field); display: flex;
  }
  .field-label {
    width: 194px; height: 100%; background: var(--tan);
    font-family: "Cinzel Decorative", Georgia, serif; font-weight: 700; font-size: 28px;
    color: var(--ink); display: flex; align-items: center; justify-content: center;
  }
  .field--message { height: 229px; background: linear-gradient(90deg, #3e0b0d 0 200px, var(--field) 200px); }
  .field--message .field-label { height: 40px; width: 186px; }

  .send {
    position: absolute; left: 717px; top: 808px; width: 165px; height: 45px;
    border: 3px solid var(--frame); background: var(--field);
    font-family: "Cinzel Decorative", Georgia, serif; font-weight: 700; font-size: 14px;
    color: var(--ink); display: flex; align-items: center; justify-content: center;
  }

  .footer-links { position: absolute; left: 408px; top: 866px; display: flex; }
  .footer-links a {
    font-size: 17px; color: var(--ink); text-decoration: none; padding: 5px 7px;
    border-left: 1px solid var(--frame);
  }
  .footer-links a:first-child { border-left: none; }
</style>
</head>
<body>
  <header class="top-bar">
    <nav class="nav">
      <a style="left:24px">The Introduction</a>
      <a style="left:199px">The Experience</a>
      <a style="left:356px">The Gentlement</a>
      <a style="left:780px">The Answer</a>
      <a style="left:913px">The Reservation</a>
      <a style="left:1075px">Get In Touch</a>
    </nav>
  </header>

  <main class="column">
    <div class="column-head"><div class="brand">Velvet Hour</div></div>
  </main>

  <svg class="ribbon" width="395" height="95" viewBox="0 0 395 95" aria-hidden="true">
    <polygon points="0,45 75,45 75,92 30,92 55,68" fill="#6b3a2c"/>
    <polygon points="395,45 320,45 320,92 365,92 340,68" fill="#6b3a2c"/>
    <path d="M72,12 Q200,-6 322,12 L322,62 Q200,48 72,62 Z" fill="#7a4a36"/>
  </svg>
  <h1 class="page-title">Get In Touch</h1>
  <p class="intro">Forward question,concerns, and pleasantries via the following form</p>

  <div class="figure" role="img" aria-label="Silhouette of a gentleman in a suit with a red-lit collar"></div>

  <form>
    <div class="field" style="top:330px"><span class="field-label">Name:</span></div>
    <div class="field" style="top:385px"><span class="field-label">Email:</span></div>
    <div class="field" style="top:443px"><span class="field-label">Phone:</span></div>
    <div class="field" style="top:506px"><span class="field-label">Subject:</span></div>
    <div class="field field--message" style="top:568px"><span class="field-label">Message:</span></div>
    <div class="send">Send Message</div>
  </form>

  <footer class="footer-links">
    <a>Privacy Policy</a><a>Terms &amp; Condition</a><a>Get In Touch</a><a>Login</a>
  </footer>
</body>
</html>
```